Corvella Santoro Winery 2023 Label

We are just about to bottle our very first Napa Valley Cabernet Sauvignon and need label ideas

Target Market(s)

Cab drinkers who like Napa California Cabs

Industry/Entity Type

Wine Making

Logo Text

Corvella Santoro 2023 Napa Estate Grown Cabernet Sauvignon

Requirements
Must have
• Winery Name, year of vintage and Napa Estate Cab
Nice to have
• If using the initials C and S use gold letters on black or red background

```html
<!DOCTYPE html>
<html lang="en">
<head>
<meta charset="UTF-8">
<title>Corvella Santoro 2023 Estate Grown Cabernet Sauvignon – Label</title>
<link href="https://fonts.googleapis.com/css2?family=Federo&display=swap" rel="stylesheet">
<style>
  :root {
    --paper: #ebe6e1;
    --paper-stain: #ddd1c4;
    --paper-light: #f1ede9;
    --gold: #9a7f4f;
  }
  * { margin: 0; padding: 0; box-sizing: border-box; }
  html, body {
    width: 1200px;
    height: 1000px;
    overflow: hidden;
    background: var(--paper);
  }
  .label {
    position: relative;
    width: 1200px;
    height: 1000px;
    overflow: hidden;
    font-family: "Federo", "Poiret One", sans-serif;
    color: var(--gold);
    text-align: center;
    background:
      radial-gradient(ellipse 320px 220px at 120px 180px, var(--paper-stain) 0%, transparent 70%),
      radial-gradient(ellipse 260px 200px at 1080px 300px, var(--paper-stain) 0%, transparent 70%),
      radial-gradient(ellipse 300px 240px at 200px 760px, var(--paper-stain) 0%, transparent 72%),
      radial-gradient(ellipse 280px 220px at 1000px 860px, var(--paper-stain) 0%, transparent 70%),
      radial-gradient(ellipse 240px 160px at 620px 120px, var(--paper-stain) 0%, transparent 75%),
      radial-gradient(ellipse 500px 400px at 600px 500px, var(--paper-light) 0%, transparent 80%),
      var(--paper);
  }
  .label__line {
    position: absolute;
    left: 0;
    width: 100%;
    line-height: 1;
    white-space: nowrap;
  }
  .vineyard-name {
    top: 82px;
    font-size: 29px;
    letter-spacing: 0.5px;
  }
  .winery-name--first {
    top: 255px;
    font-size: 88px;
    letter-spacing: 1px;
  }
  .winery-name--second {
    top: 360px;
    font-size: 100px;
    letter-spacing: 1px;
  }
  .vintage {
    top: 455px;
    font-size: 210px;
    letter-spacing: 2px;
  }
  .wine-style {
    top: 655px;
    font-size: 64px;
  }
  .varietal {
    top: 716px;
    font-size: 48px;
  }
  .region {
    top: 914px;
    font-size: 31px;
    letter-spacing: 1px;
  }
</style>
</head>
<body>
  <main class="label">
    <p class="label__line vineyard-name">CORVELLA SANTORO VINEYARDS</p>
    <h1>
      <span class="label__line winery-name--first">CORVELLA</span>
      <span class="label__line winery-name--second">SANTORO</span>
    </h1>
    <p class="label__line vintage">2023</p>
    <p class="label__line wine-style">ESTATE GROWN</p>
    <p class="label__line varietal">CABERNET SAUVIGNON</p>
    <p class="label__line region">NAPA</p>
  </main>
</body>
</html>
```